Waste Oil Filter collection & disposal

Basically I need a 1 page website for the business called Brenmoor Waste Solutions.
We are a environmental service provider and we collect and dispose of waste oil filters to protect the environment from hazardous waste oil products.

This is the link to our current website: www.brenmoorwaste.co.nz

we want it to look fresh and better than our current website. we may potentially look at getting a new logo designed and are open to ideas/designs if you have any.

Industry/Entity Type

Business

Logo Text

Brenmoor Waste Solutions

Number of Pages Required

1 page

Requirements
Must have
• same colours as current website.
• description of what service we provide please refer to leaflet attached

```html
<!DOCTYPE html>
<html lang="en">
<head>
<meta charset="utf-8">
<title>Brenmoor Waste Solutions Ltd</title>
<link href="https://fonts.googleapis.com/css2?family=Montserrat:wght@400;600;700&family=Questrial&display=swap" rel="stylesheet">
<style>
:root{
  --green:#5e9467;
  --green-dark:#4f8759;
  --green-light:#b5cdb7;
  --teal:#4e7f77;
  --navy:#1c2266;
  --grey:#e5e5e2;
  --map-grey:#dcdfd9;
  --white:#ffffff;
  --text-dark:#1b1b1b;
}
*{margin:0;padding:0;box-sizing:border-box}
html,body{width:1200px;height:2605px;overflow:hidden;background:var(--white)}
body{position:relative;font-family:"Questrial",sans-serif;color:var(--text-dark)}
.abs{position:absolute}

/* top bar */
.topbar{left:0;top:0;width:1200px;height:34px;background:rgba(255,255,255,.75);z-index:5}
.topbar .email,.topbar .phone{top:7px;font-family:"Montserrat",sans-serif;font-size:15px;color:var(--navy);display:flex;align-items:center;gap:8px}
.topbar .email{left:128px}
.topbar .phone{left:955px}
.nav{left:396px;top:6px;font-family:"Montserrat",sans-serif;font-weight:700;font-size:17px;color:var(--navy)}
.nav a{color:inherit;text-decoration:none;position:absolute;white-space:nowrap}

/* hero */
.hero{left:0;top:0;width:1200px;height:752px;background:linear-gradient(160deg,#3d5a34 0%,#6f8f55 30%,#c9cfcb 55%,#8aa08c 75%,#4f6a4a 100%)}
.hero-overlay{left:0;top:0}
.brand-box{left:483px;top:52px;width:238px;height:88px;background:var(--white);z-index:6;padding:8px 10px;text-align:center}
.brand-box .name{font-family:"Montserrat",sans-serif;font-weight:700;font-size:21px;line-height:1.05;color:var(--navy)}
.brand-box .tag{font-size:11px;color:var(--navy);margin-top:6px}
.hero-mini{left:944px;top:516px;font-family:"Montserrat",sans-serif;font-weight:700;font-size:16px;line-height:1.15;color:var(--white);z-index:6}
.hero-head{right:13px;top:578px;text-align:right;font-weight:400;font-size:34px;line-height:38px;color:var(--white);z-index:6}

/* intro */
.intro{left:60px;top:783px;width:1080px;text-align:center;font-family:"Montserrat",sans-serif;font-weight:700;font-size:19px;line-height:26px;color:var(--navy);z-index:3}

/* cards */
.card{top:868px;width:271px;height:371px;background:var(--green-light);text-align:center;color:var(--text-dark);font-size:24px;line-height:30px;z-index:3}
.card .photo{position:absolute;left:27px;top:18px;width:217px;height:165px}
.card p{position:absolute;left:6px;right:6px;top:196px}
.card.featured{background:var(--green);color:var(--white);box-shadow:0 4px 12px rgba(0,0,0,.35);top:864px;height:376px}
.card.featured .photo{border:6px solid #e9ece8}
.card.alt .photo{background:var(--green-dark)}

/* process */
.process{left:0;top:1268px;width:1200px;height:394px;background:var(--green);text-align:center;color:var(--white)}
.process h2{margin-top:20px;font-family:"Montserrat",sans-serif;font-weight:700;font-size:27px;color:var(--navy)}
.process .lead{margin-top:14px;font-size:24px;line-height:30px;font-style:italic;color:#e6efe6}
.process ol{list-style:none;margin-top:6px;font-family:"Montserrat",sans-serif;font-weight:600;font-size:23px;line-height:30px;letter-spacing:.5px}
.process ol .hl{color:#1d5c45}

/* oil */
.oil{left:0;top:1668px;width:1200px;height:242px;background:var(--grey);text-align:center}
.oil h2{margin-top:8px;font-family:"Montserrat",sans-serif;font-weight:700;font-size:27px;color:var(--navy)}
.oil p{font-size:23px;line-height:28px;color:var(--navy)}
.quote{width:218px;height:218px;border-radius:50%;background:var(--green);border:6px solid var(--white);display:flex;flex-direction:column;justify-content:center;align-items:center;padding:0 22px;text-align:center;color:var(--white);font-family:"Montserrat",sans-serif;font-weight:600;font-size:15px;line-height:19px;z-index:3}
.quote cite{font-family:"Questrial",sans-serif;font-weight:400;font-size:16px;line-height:18px;font-style:italic;color:#e3ece3}

/* pricing */
.ready{left:0;top:2125px;width:1200px;text-align:center;font-family:"Montserrat",sans-serif;font-weight:700;font-size:28px;color:var(--navy)}
.prices{left:358px;top:2185px;width:481px;height:129px;background:var(--green);z-index:3;text-align:center;color:var(--white);font-family:"Montserrat",sans-serif;font-weight:600;font-size:23px;line-height:42px;padding-top:2px}

/* footer */
.footer-brand{left:44px;top:2408px;font-family:"Montserrat",sans-serif;font-weight:700;font-size:15px;line-height:17px;color:var(--navy);z-index:3}
.footer-links{left:80px;top:2456px;font-family:"Montserrat",sans-serif;font-weight:600;font-size:13px;line-height:30px;color:var(--navy);z-index:3;text-align:center}
.copyright{left:38px;top:2517px;font-size:12px;line-height:15px;color:#e8efee;z-index:3;text-align:center}
.map{left:950px;top:2338px;width:242px;height:150px;background:var(--white);border:4px solid #f2f2f2;z-index:3;box-shadow:0 1px 4px rgba(0,0,0,.3)}
.map .area{position:absolute;left:0;top:0;width:234px;height:117px;background:var(--map-grey)}
.map .bar{position:absolute;left:0;bottom:0;width:234px;height:25px;background:var(--green);display:flex;font-family:"Montserrat",sans-serif;font-size:11px;color:var(--white)}
.map .bar span{flex:1;display:flex;align-items:center;justify-content:center;border-right:1px solid rgba(255,255,255,.5)}
.map .bar span+span{flex:2;border-right:0}
.hours{left:1050px;top:2500px;width:140px;text-align:right;font-family:"Montserrat",sans-serif;font-weight:700;font-size:11px;line-height:14px;color:var(--white);z-index:3}
</style>
</head>
<body>

<div class="abs hero" role="img" aria-label="Photo of the green and white oil filter collection truck parked on grass in front of trees"></div>
<svg class="abs hero-overlay" width="1200" height="1240" viewBox="0 0 1200 1240" aria-hidden="true" style="z-index:2">
  <polygon points="1200,330 1200,752 380,752" fill="rgba(94,148,103,.8)"/>
  <polygon points="1200,250 1200,340 950,500" fill="rgba(181,205,183,.5)"/>
  <polygon points="1200,752 1200,780 590,1060 1045,752" fill="var(--green-light)"/>
</svg>

<div class="abs topbar">
  <div class="abs email">
    <svg width="20" height="14" viewBox="0 0 20 14"><rect x="1" y="1" width="18" height="12" fill="none" stroke="#1c2266" stroke-width="1.6"/><polyline points="1,1 10,8 19,1" fill="none" stroke="#1c2266" stroke-width="1.6"/></svg>
    info@brenmoorwaste.co.nz
  </div>
  <nav class="abs nav">
    <a style="left:0">HOME</a>
    <a style="left:85px">ABOUT</a>
    <a style="left:181px">GALLERY</a>
    <a style="left:292px">CONTACT US</a>
  </nav>
  <div class="abs phone">
    <svg width="18" height="18" viewBox="0 0 18 18"><circle cx="9" cy="9" r="8" fill="none" stroke="#1c2266" stroke-width="1.5"/><path d="M6 5l2 0 1 2-1 1c.5 1 1.5 2 2.5 2.5l1-1 2 1 0 2c-4 0-7.5-3.5-7.5-7.5z" fill="#1c2266"/></svg>
    06 555 0142
  </div>
</div>

<div class="abs brand-box">
  <div class="name">Brenmoor Waste<br>Solutions Ltd</div>
  <div class="tag">Oil Filter Collection &amp; Disposal Service</div>
</div>

<div class="abs hero-mini">Brenmoor Waste<br>Solutions</div>
<h1 class="abs hero-head">Brenmoor Waste Solutions Ltd<br>service the Lower North Island and<br>specialise in the collection<br>&amp; disposal of oil &amp; fuel filters</h1>

<p class="abs intro">We offer a cost effective environmentally friendly system for the collection and disposal of waste oil<br>filters helping minimise contamination of landfills keeping your industry compliant.</p>

<div class="abs card" style="left:14px">
  <div class="photo" role="img" aria-label="Photo of the filter processing workshop with machinery" style="background:linear-gradient(135deg,#8b9aa6,#3f7a6a 60%,#5c6a60)"></div>
  <p>We are passionate<br>about doing<br>our bit in keeping<br>New Zealand<br>Clean and Green.</p>
</div>
<div class="abs card featured" style="left:318px">
  <div class="photo" role="img" aria-label="Photo of used oil filters on the processing line" style="background:linear-gradient(135deg,#6f7a78,#2f6e5c 55%,#9aa3a0)"></div>
  <p>Our processes are<br>environmentally<br>friendly &amp; minimise<br>the contamination<br>of landfills.</p>
</div>
<div class="abs card alt" style="left:611px">
  <div class="photo" role="img" aria-label="Photo of a black wheelie collection bin" style="background:linear-gradient(180deg,#5a8c63,#4f8759)"></div>
  <p>We offer a cost<br>effective system<br>for the collection<br>and disposal of<br>waste oil filters.</p>
</div>
<div class="abs card" style="left:915px">
  <div class="photo" role="img" aria-label="Photo of the green filter crushing press" style="background:linear-gradient(135deg,#c9cfcb,#2f8a68 55%,#b9a988)"></div>
  <p>We keep your<br>industry compliant.</p>
</div>

<section class="abs process">
  <h2>The Process</h2>
  <p class="lead">Filters are collected and transported back<br>to the processing plant.<br><br>At the processing plant they are:</p>
  <ol>
    <li>Drained</li>
    <li>Sorted</li>
    <li class="hl">Drained again</li>
    <li>Crushed into bricks</li>
    <li>Drained a third time</li>
    <li>Stacked ready for Metal Recycling</li>
  </ol>
</section>

<section class="abs oil">
  <h2>What Happens to the Oil</h2>
  <p>All residual oil is collected into our tank<br>and then recycled.<br>Currently we are processing over 2,000<br>litres of oil a month</p>
</section>
<div class="abs quote" style="left:224px;top:1818px">"Each used oil filter has on average, more than quarter of a litre of used motor oil "<cite>- EcoCycle Trust</cite></div>
<div class="abs quote" style="left:490px;top:1884px">"Recycling engine oil protects the environment and conserves energy resources "<cite>- Oil Recycling</cite></div>
<div class="abs quote" style="left:760px;top:1818px">"one litre of used oil can contaminate one million litres of water "<cite>- Harbourside City Council</cite></div>

<h2 class="abs ready">Ready to help you</h2>
<svg class="abs" style="left:0;top:2140px;z-index:2" width="1200" height="465" viewBox="0 0 1200 465" aria-hidden="true">
  <polygon points="839,2 839,45 560,45" fill="var(--green-light)"/>
  <polygon points="358,174 358,218 620,174" fill="var(--green-light)"/>
  <polygon points="0,222 0,465 470,465" fill="var(--teal)"/>
  <polygon points="1200,110 1200,465 420,465" fill="var(--green)"/>
</svg>
<div class="abs prices">
  <div>Monthly Bin Collection: $65.00</div>
  <div>Additional Bins: $35.00 ea</div>
  <div>Account Set Up Fee: $85.00</div>
</div>

<div class="abs footer-brand">Brenmoor Waste<br>Solutions</div>
<div class="abs footer-links">Privacy<br>Log In</div>
<div class="abs copyright">© 2017 Brenmoor Waste<br>Solutions Ltd</div>

<div class="abs map">
  <div class="area" role="img" aria-label="Location map of the processing plant"></div>
  <div class="bar"><span>ZOOM</span><span>GET DIRECTIONS</span></div>
</div>
<div class="abs hours">OPENING HOURS<br>Monday - Friday<br>7.30am - 5.00pm</div>

</body>
</html>
```